psd/html for a e Pennoria Payment website designed

hi
i am in need of a psd / html for a whole website designed
the site is a e wallet /payment system i can i will provide a link to what type of style i am looking for but i can not stress this enough i do not want anyone replicating the website i am just providing the links to show you what kind of function and the content that is involved also, i have a srs with detailed pages you can read and refer to if need be
thanks of viewing
Vantoleaf.com
Brisklune.com
marblequivercoin.com
Qrdelivane.com

```html
<!DOCTYPE html>
<html lang="en">
<head>
<meta charset="utf-8">
<title>Pennoria Payment System</title>
<link href="https://fonts.googleapis.com/css2?family=Montserrat:wght@400;500;600;700&family=Arimo&family=Noto+Serif:ital@1&display=swap" rel="stylesheet">
<style>
:root{
  --blue:#1a9ee0;
  --blue-dark:#0b80c2;
  --blue-text:#0d8bd2;
  --ink:#222;
  --body:#333;
  --muted:#aaa;
  --line:#dcdcdc;
  --hero-a:#c7ddf4;
  --hero-b:#eaf3fc;
}
*{margin:0;padding:0;box-sizing:border-box}
html,body{width:1042px;height:1200px;overflow:hidden;background:#fff}
body{position:relative;font-family:"Montserrat",sans-serif;color:var(--body)}
a{text-decoration:none;color:inherit}
.abs{position:absolute}

.site-header{position:absolute;left:0;top:0;width:1042px;height:126px;background:linear-gradient(#f8f8f8,#e9e9e9);border-bottom:1px solid #d6d6d6}
.brand{left:120px;top:20px;display:flex;align-items:center;gap:8px}
.brand-dot{width:62px;height:62px;border-radius:50%;background:var(--blue-dark)}
.brand-text{display:flex;flex-direction:column}
.brand-name{font-weight:700;font-size:34px;line-height:36px;color:var(--blue-dark)}
.brand-tag{font-weight:700;font-size:15px;color:#555;letter-spacing:.3px}
.phone{right:126px;top:12px;font-family:"Arimo",sans-serif;font-size:15px;color:var(--ink)}
.search{left:485px;top:44px;width:235px;height:28px;border:1px solid #ccc;border-radius:14px;background:#fff;font-size:12px;color:#555;padding:6px 13px}
.search svg{position:absolute;right:8px;top:4px}
.btn{display:flex;align-items:center;justify-content:center;font-weight:700;border-radius:4px}
.btn-blue{background:linear-gradient(#1fa6ec,#0a6fb8);color:#fff;box-shadow:0 3px 0 #064f86}
.btn-yellow{background:linear-gradient(#ffe23a,#f7b500);color:#1a1a1a;box-shadow:0 3px 0 #c98900}
.head-login{left:736px;top:41px;width:83px;height:30px;font-size:15px}
.head-signup{left:828px;top:41px;width:91px;height:30px;font-size:15px}

.main-nav{left:122px;top:102px;width:797px;height:43px;background:var(--blue);border-radius:3px;display:flex;overflow:hidden}
.main-nav a{display:flex;align-items:center;justify-content:center;color:#fff;font-weight:600;font-size:12.5px;border-right:1px solid #3bb2ea;white-space:nowrap}
.main-nav a:last-child{border-right:0}
.main-nav .active{background:var(--blue-dark)}

.hero{left:122px;top:161px;width:797px;height:314px;background:linear-gradient(160deg,var(--hero-a),var(--hero-b) 70%);border-radius:3px;box-shadow:0 14px 14px -12px rgba(0,0,0,.35)}
.hero h1{position:absolute;left:25px;top:38px;font-size:40px;line-height:41px;font-weight:700;color:var(--blue-text)}
.hero p{position:absolute;left:25px;top:151px;width:320px;font-family:"Arimo",sans-serif;font-size:14px;line-height:19px;color:#111}
.hero-cta{left:28px;top:233px;width:172px;height:42px;font-size:20px}
.hero-art{left:425px;top:8px;width:285px;height:300px;border-radius:8px;background:radial-gradient(circle at 50% 55%,#3aa84a 0,#f39a1e 30%,rgba(120,190,235,.5) 60%,rgba(234,243,252,0) 75%)}

.feature{top:508px;width:253px}
.feature h2{font-size:20px;font-weight:500;color:var(--blue-text);margin-bottom:13px;line-height:24px}
.feature-frame{height:127px;background:#e2e2e2;padding:8px}
.feature-img{width:100%;height:100%}
.feature p{margin-top:17px;font-size:11.9px;line-height:19px;color:var(--body);letter-spacing:-.1px}
.learn{display:inline-block;margin-top:8px;padding:6px 9px;border:1px solid #ccc;border-radius:3px;background:linear-gradient(#fff,#f0f0f0);font-size:12.5px;color:var(--blue-text)}

.rule{left:122px;width:797px;height:1px;background:var(--line)}
.cta-login{left:354px;top:886px;width:155px;height:42px;font-size:20px}
.cta-signup{left:532px;top:886px;width:155px;height:42px;font-size:20px}
.star{left:513px}
.quote{left:232px;top:970px;width:636px;text-align:center;font-family:"Noto Serif",serif;font-style:italic;font-size:20px;line-height:26px;color:var(--muted)}

.footer-nav{left:122px;top:1143px;font-size:12px;color:var(--blue-text);white-space:nowrap}
.footer-nav span{color:#888;margin:0 7px}
.copyright{left:123px;top:1172px;font-size:11px;color:#333}
.trust{top:1140px;display:flex;gap:8px;align-items:center}
.trust i{display:block;border-radius:3px}
.social{left:813px;top:1140px;display:flex;gap:9px}
.social i{display:block;width:20px;height:20px;border-radius:50%;background:#666}
</style>
</head>
<body>

<header class="site-header">
  <div class="brand abs"><div class="brand-dot"></div><div class="brand-text"><span class="brand-name">Pennoria</span><span class="brand-tag">PAYMENT SYSTEM</span></div></div>
  <div class="phone abs">0800 246810 (Freephone) | Contact</div>
  <div class="search abs">Search
    <svg width="22" height="22" viewBox="0 0 22 22"><circle cx="12" cy="9" r="6" fill="none" stroke="#555" stroke-width="2"/><line x1="8" y1="13" x2="3" y2="18" stroke="#555" stroke-width="3"/></svg>
  </div>
  <a class="btn btn-blue head-login abs" href="#">LOGIN</a>
  <a class="btn btn-yellow head-signup abs" href="#">SIGN UP</a>
</header>

<nav class="main-nav abs">
  <a class="active" href="#" style="width:68px">HOME</a>
  <a href="#" style="width:174px">PERSONAL ACCOUNTS</a>
  <a href="#" style="width:168px">BUSINESS ACCOUNTS</a>
  <a href="#" style="width:151px">BEGINNER'S GUIDE</a>
  <a href="#" style="width:115px">DEVELOPERS</a>
  <a href="#" style="width:121px">HELP CENTRE</a>
</nav>

<section class="hero abs">
  <h1>Lorem ipsum<br>dolor sit amet</h1>
  <p>Sed ut perspiciatis unde omnis iste natus error sit voluptatem accusantium doloremque laudantium.</p>
  <a class="btn btn-yellow hero-cta abs" href="#">SIGN UP NOW</a>
  <div class="hero-art abs" role="img" aria-label="Laptop with a shopping bag on screen surrounded by shopping icons"></div>
</section>

<article class="feature abs" style="left:122px">
  <h2>Shopping Online</h2>
  <div class="feature-frame"><div class="feature-img" role="img" aria-label="Glowing shopping cart on a blue circuit background" style="background:linear-gradient(135deg,#0a1d4a,#1d6fd0 60%,#0a2a66)"></div></div>
  <p>Lorem ipsum dolor sit amet, consectetur adipisicing elit, sed do eiusmod tempor incididunt ut labore et dolore magna aliqua. Lorem ipsum dolor sit amet, consectetur adipisicing elit, sed do eiusmod tempor incididunt ut labore.</p>
  <a class="learn" href="#">Learn more</a>
</article>

<article class="feature abs" style="left:394px">
  <h2>Selling Online</h2>
  <div class="feature-frame"><div class="feature-img" role="img" aria-label="Shopping cart linked to colourful commerce icons" style="background:linear-gradient(90deg,#f1efe6,#f5d9b8 50%,#cde6ea)"></div></div>
  <p>Lorem ipsum dolor sit amet, consectetur adipisicing elit, sed do eiusmod tempor incididunt ut labore et dolore magna aliqua. Lorem ipsum dolor sit amet, consectetur adipisicing elit, sed do eiusmod tempor incididunt ut labore.</p>
  <a class="learn" href="#">Learn more</a>
</article>

<article class="feature abs" style="left:667px">
  <h2>News</h2>
  <div class="feature-frame"><div class="feature-img" role="img" aria-label="Hand drawing a rising bar chart" style="background:linear-gradient(135deg,#4cc3d6,#8fdbe6)"></div></div>
  <p>Lorem ipsum dolor sit amet, consectetur adipisicing elit, sed do eiusmod tempor incididunt ut labore et dolore magna aliqua. Lorem ipsum dolor sit amet, consectetur adipisicing elit, sed do eiusmod tempor incididunt ut labore.</p>
  <a class="learn" href="#">Learn more</a>
</article>

<div class="rule abs" style="top:861px"></div>
<a class="btn btn-yellow cta-login abs" href="#">LOGIN</a>
<a class="btn btn-blue cta-signup abs" href="#">SIGN UP</a>

<div class="rule abs" style="top:958px"></div>
<svg class="star abs" style="top:950px" width="14" height="14" viewBox="0 0 14 14"><polygon points="7,1 8.8,5.2 13,5.4 9.7,8.2 10.8,12.6 7,10.1 3.2,12.6 4.3,8.2 1,5.4 5.2,5.2" fill="#bbb"/></svg>
<blockquote class="quote abs">Lorem ipsum dolor sit amet, consectetur adipisicing elit, sed do eiusmod tempor incididunt ut labore et dolore magna aliqua. Lorem ipsum dolor sit amet, consectetur adipisicing elit, sed do eiusmod tempor incididunt ut labore.</blockquote>
<div class="rule abs" style="top:1090px"></div>
<svg class="star abs" style="top:1085px" width="14" height="14" viewBox="0 0 14 14"><polygon points="7,1 8.8,5.2 13,5.4 9.7,8.2 10.8,12.6 7,10.1 3.2,12.6 4.3,8.2 1,5.4 5.2,5.2" fill="#bbb"/></svg>

<div class="rule abs" style="top:1126px"></div>
<footer>
  <nav class="footer-nav abs"><a href="#">Home</a><span>|</span><a href="#">Merchants</a><span>|</span><a href="#">Exchangers</a><span>|</span><a href="#">Fees</a><span>|</span><a href="#">Terms</a><span>|</span><a href="#">F.A.Q.</a><span>|</span><a href="#">Developers</a></nav>
  <div class="copyright abs">© 2013 Pennoria Payment</div>
  <div class="trust abs" style="left:607px">
    <i style="width:62px;height:34px;background:#d9d9d9"></i>
    <i style="width:50px;height:26px;background:#f4c9a0"></i>
    <i style="width:62px;height:30px;background:#c9d6ea"></i>
  </div>
  <div class="social abs"><i></i><i></i><i></i><i></i></div>
</footer>

</body>
</html>
```